Envelope Design Project

I will need two envelopes to be designed:-

DL size
C4 size

Please see uploaded documents for Design specs:

1) Design specs provided by printer (doc called DL Envelope Specs)
2) Design specs to comply with Kestrel Mailways requirements (doc called Kestrel Mailways Envelope Design Requirements)

Please adhere to the above for final design. Many thanks.

Target Market(s)

Real Estate Agents, Strata Managers, Builders, Architects, Business Owners

Industry/Entity Type

Printer

Requirements
Must have
• In top left corner
- Logo
- Return address - Suite 5, 19 Wattlebark Rd, Marrowick, NSW 2417

```html
<!DOCTYPE html>
<html lang="en">
<head>
<meta charset="utf-8">
<title>Corvan Asbestos &amp; Safety – Envelope Set</title>
<link href="https://fonts.googleapis.com/css2?family=Questrial&display=swap" rel="stylesheet">
<style>
  :root {
    --canvas-bg: #ededed;
    --paper: #e3e3e3;
    --band-top: #29223f;
    --band-bottom: #3d3270;
    --ink-navy: #2a2450;
    --accent-green: #8db52b;
    --address-grey: #555;
    --logo-panel: #f4f4f4;
  }
  * { margin: 0; padding: 0; box-sizing: border-box; }
  html, body { width: 1200px; height: 1000px; overflow: hidden; }
  body {
    background: var(--canvas-bg);
    font-family: "Questrial", "Century Gothic", sans-serif;
    position: relative;
  }
  .envelope {
    position: absolute;
    background: var(--paper);
    overflow: hidden;
  }
  .envelope--c4 { left: 290px; top: 115px; width: 660px; height: 466px; }
  .envelope--dl-front { left: 120px; top: 678px; width: 457px; height: 228px; }
  .envelope--dl-back { left: 647px; top: 678px; width: 457px; height: 228px; }

  .side-band {
    position: absolute; left: 0; top: 0; bottom: 0;
    background: linear-gradient(180deg, var(--band-top), var(--band-bottom));
  }
  .envelope--c4 .side-band { width: 79px; }
  .envelope--dl-front .side-band { width: 65px; }

  .logo-panel {
    position: absolute;
    background: var(--logo-panel);
    border-radius: 8px;
    display: flex; align-items: center;
    color: var(--ink-navy);
  }
  .logo-mark {
    background: var(--accent-green);
    border-radius: 3px;
    flex: none;
  }
  .logo-name { line-height: 1; }
  .logo-name .name-main { display: block; }
  .logo-name .name-sub { display: block; letter-spacing: 0.02em; }

  .envelope--c4 .logo-panel { left: 36px; top: 35px; width: 160px; height: 82px; padding-left: 14px; gap: 9px; }
  .envelope--c4 .logo-mark { width: 18px; height: 18px; }
  .envelope--c4 .name-main { font-size: 34px; }
  .envelope--c4 .name-sub { font-size: 12.5px; margin-top: 6px; }

  .envelope--dl-front .logo-panel { left: 30px; top: 27px; width: 130px; height: 68px; padding-left: 11px; gap: 7px; }
  .envelope--dl-front .logo-mark { width: 14px; height: 14px; }
  .envelope--dl-front .name-main { font-size: 27px; }
  .envelope--dl-front .name-sub { font-size: 10px; margin-top: 5px; }

  .return-address {
    position: absolute;
    color: var(--address-grey);
    text-align: right;
    line-height: 1.45;
  }
  .envelope--c4 .return-address { left: 90px; top: 129px; width: 98px; font-size: 8.5px; }
  .envelope--dl-front .return-address { left: 70px; top: 104px; width: 96px; font-size: 6.5px; }

  .flap {
    position: absolute; left: 0; top: 0; width: 100%; height: 67px;
    background: linear-gradient(180deg, var(--band-top), var(--band-bottom));
    border-radius: 0 0 22px 22px;
  }
</style>
</head>
<body>
  <section class="envelope envelope--c4" aria-label="C4 envelope front">
    <div class="side-band"></div>
    <div class="logo-panel">
      <span class="logo-mark"></span>
      <span class="logo-name">
        <span class="name-main">Corvan</span>
        <span class="name-sub">ASBESTOS &amp; SAFETY</span>
      </span>
    </div>
    <p class="return-address">Suite 5, 19 Wattlebark Rd<br>Marrowick, NSW 2417</p>
  </section>

  <section class="envelope envelope--dl-front" aria-label="DL envelope front">
    <div class="side-band"></div>
    <div class="logo-panel">
      <span class="logo-mark"></span>
      <span class="logo-name">
        <span class="name-main">Corvan</span>
        <span class="name-sub">ASBESTOS &amp; SAFETY</span>
      </span>
    </div>
    <p class="return-address">Suite 5, 19 Wattlebark Rd<br>Marrowick, NSW 2417</p>
  </section>

  <section class="envelope envelope--dl-back" aria-label="DL envelope back">
    <div class="flap"></div>
  </section>
</body>
</html>
```